Our desktop web app builder needs a redesign

We want to redesign our low-code web app builder called Vorlix. Vorlix runs in desktop environments and is aimed at IT professionals and developers.

The UI consists of a button bar, multiple panels and a tabbed working area. We are looking to completely change the look and feel of the application interfaces, while keeping the layout and functionality the same.

We would like to see your ideas for fonts, sizing, colour, icons and any other visual UI element. Your work can be a rough mockup of your design ideas, and does not need to be pixel perfect. Legibility and optimised use of space are key.

More details about the app and how it works here: https://vorlix.example/

If we like your ideas, we will get in touch with you and work with you to develop the new design in greater detail.

```html
<!DOCTYPE html>
<html lang="en">
<head>
<meta charset="utf-8">
<title>Vorlix Designer – UI concepts</title>
<link href="https://fonts.googleapis.com/css2?family=Roboto:wght@400;500;700&family=Montserrat:wght@700&family=Roboto+Slab:wght@500&display=swap" rel="stylesheet">
<style>
:root{
  --canvas:#d9d9d9;
  --titlebar:#3a3a3a;
  --toolbar:#454545;
  --panel:#4b4b4b;
  --panel-2:#575757;
  --footer:#343434;
  --cyan:#00c9ea;
  --white:#ffffff;
  --tile:#f1f1f1;
  --line:#dcdcdc;
  --text:#222222;
  --muted:#7a7a7a;
  --light-text:#e8e8e8;
  --valid-bg:#e7f8fc;
  --error:#e0282e;
}
*{box-sizing:border-box;margin:0;padding:0}
html,body{width:1200px;height:3186px;overflow:hidden}
body{background:var(--canvas);font-family:'Roboto',sans-serif;color:var(--text);position:relative}
.frame{position:absolute;left:64px;width:1070px;background:var(--white);box-shadow:0 2px 6px rgba(0,0,0,.18);overflow:hidden}
.titlebar{position:absolute;left:0;top:0;width:100%;height:32px;background:var(--titlebar);color:var(--light-text);font-size:12px}
.titlebar .brand{position:absolute;left:14px;top:9px;display:flex;align-items:center;gap:5px;font-size:11px;font-weight:500;color:var(--cyan);line-height:14px}
.titlebar .brand i{display:block;width:9px;height:9px;border-radius:50%;background:var(--cyan)}
.win-btns{position:absolute;right:28px;top:3px;display:flex;gap:4px}
.win-btns span{width:24px;height:16px;background:#2b2b2b;display:flex;align-items:center;justify-content:center;color:#fff;font-size:11px}
.win-btns .max::before{content:"";width:9px;height:8px;border:1px solid #fff}
.footer{position:absolute;left:0;bottom:0;width:100%;height:54px;background:var(--footer);color:#f0f0f0;font-size:11px;display:flex;align-items:center;justify-content:center}
.footer .ver{position:absolute;right:28px;font-size:9px}
.win-title{position:absolute;left:82px;top:9px;font-size:12px}

.menu{position:absolute;left:86px;top:9px;display:flex;gap:17px}
.menu span{font-size:12px}
.doc-title{position:absolute;left:0;width:100%;text-align:center;top:9px;font-size:12px}
.toolbar{position:absolute;left:0;top:32px;width:100%;height:48px;background:var(--toolbar)}
.toolbar svg{position:absolute;top:14px}
.side{position:absolute;top:80px;height:726px;background:var(--panel)}
.tabhead{position:absolute;top:2px;height:31px;background:#2f2f2f}
.tab{position:absolute;top:2px;height:31px;background:var(--cyan);color:#fff;font-size:11px;font-weight:500;display:flex;align-items:center;padding-left:11px}
.tab-icons{position:absolute;top:11px;display:flex;gap:6px;color:#fff;font-size:10px}
.tab-icons svg{display:block}
.bugbear{position:absolute;left:0;top:51px;width:240px;height:37px;background:linear-gradient(90deg,#f4f4f4 0%,#e8e8e8 55%,rgba(75,75,75,1) 100%);border-left:3px solid var(--cyan);color:var(--cyan);font-size:13px;font-weight:500;padding-left:32px;line-height:37px}
.tree-row{position:absolute;height:20px;line-height:20px;color:#f2f2f2;font-size:13px;display:flex;align-items:center;gap:7px}
.chev{font-size:10px;color:#ddd;width:10px}
.ico{width:12px;height:12px;display:inline-block}

.work{position:absolute;left:249px;top:80px;width:574px;height:505px;background:var(--white)}
.box{position:absolute;border:1px solid var(--line);background:var(--white)}
.box.shadowed{box-shadow:0 1px 3px rgba(0,0,0,.12)}
.boxlabel{position:absolute;font-size:11px;font-weight:500;display:flex;align-items:center;gap:7px;color:#222}
.sq{display:inline-block;width:9px;height:9px;background:#111}
.cell{position:absolute;height:32px;border:1px solid var(--line);background:#fff;box-shadow:0 1px 2px rgba(0,0,0,.08);font-size:11px;font-weight:500;display:flex;align-items:center;justify-content:center;gap:8px;white-space:nowrap;overflow:hidden}
.t{font-family:'Roboto Slab',serif;font-size:13px;font-weight:500}
.grid-ico{width:11px;height:9px;border:1px solid #222;background:linear-gradient(#222,#222) 0 3px/100% 1px no-repeat,linear-gradient(#222,#222) 0 6px/100% 1px no-repeat,linear-gradient(#222,#222) 4px 0/1px 100% no-repeat}

.valid{position:absolute;left:249px;top:585px;width:574px;height:221px;background:var(--valid-bg)}
.valid .bar{position:absolute;left:0;top:0;width:100%;height:37px;background:#2f2f2f}
.valid .tab{top:0;height:37px;width:115px;justify-content:center;padding:0}
.vrow{position:absolute;left:0;width:100%;font-size:10.5px;color:#8a8a8a}
.vrow .x{position:absolute;left:17px;color:var(--error);font-weight:700}
.vrow .d{position:absolute;left:46px}
.vrow .p{position:absolute;left:242px}
.vhead{position:absolute;top:62px;font-size:11px;font-weight:500;color:#222}

.rightp{left:823px;width:247px;background:var(--panel-2)}
.section{position:absolute;left:2px;width:243px;height:32px;background:#3d3d3d;color:#fff;font-size:13px;display:flex;align-items:center;justify-content:center}
.tiles{position:absolute;left:2px;display:grid;grid-template-columns:repeat(4,60px);gap:1px}
.tile{height:43px;background:var(--tile);font-size:10.5px;color:#333;display:flex;flex-direction:column;align-items:center;justify-content:center;gap:3px;white-space:nowrap}
.tile.active{background:var(--cyan);color:#fff}
.tile svg{width:12px;height:12px}
.prop{position:absolute;left:4px;width:239px;height:24px;display:flex;align-items:center;color:#f2f2f2;font-size:11px}
.prop .v{position:absolute;left:92px;height:22px;background:#f2f2f2;color:#666;font-size:10.5px;display:flex;align-items:center;padding-left:8px}
.prop .chk{position:absolute;left:92px;width:23px;height:23px;background:#f2f2f2}
.help{position:absolute;left:4px;top:623px;width:117px;height:33px;background:#fff;font-size:11px;font-weight:500;display:flex;align-items:center;padding-left:9px}

.dialog-title{position:absolute;left:106px;top:97px;font-family:'Montserrat',sans-serif;font-weight:700;font-size:25px;letter-spacing:.5px}
.card{position:absolute;left:106px;width:860px;border:2px solid #ececec;background:#fff}
.field{position:absolute;height:44px;border:1px solid var(--line);font-size:13.5px;color:var(--muted);display:flex;align-items:center;padding-left:13px;background:#fff}
.field .drop{position:absolute;right:0;top:0;width:43px;height:100%;border-left:1px solid var(--line);display:flex;align-items:center;justify-content:center}
.flabel{position:absolute;font-size:15.5px;font-weight:500;color:#111}
.btn-primary{position:absolute;background:var(--cyan);color:#fff;font-size:13.5px;font-weight:500;display:flex;align-items:center;justify-content:center}
.btn-outline{position:absolute;border:2px solid var(--cyan);color:var(--cyan);font-size:13.5px;font-weight:500;display:flex;align-items:center;justify-content:center;background:#fff}
.help-text{position:absolute;font-size:13.5px;color:#555}
.expander{position:absolute;font-size:15.5px;font-weight:500;display:flex;align-items:center;gap:10px}
.picker{position:absolute;left:541px;width:389px;height:172px;border:1px solid var(--line);background:#fff;font-size:12.5px;color:#222;box-shadow:0 2px 4px rgba(0,0,0,.06)}
.picker div{position:absolute;display:flex;align-items:center;gap:9px}
.x2{font-family:'Roboto Slab',serif;font-weight:500;font-size:15px}
.leaf{color:#666}
</style>
</head>
<body>

<section class="frame" style="top:64px;height:860px;background:var(--panel)">
  <header class="titlebar">
    <div class="brand"><i></i>Vorlix</div>
    <nav class="menu"><span>File</span><span>Edit</span><span>Insert</span><span>Run</span><span>Window</span><span>Help</span></nav>
    <div class="doc-title">Appwithtable_stable - Vorlix Designer</div>
    <div class="win-btns"><span class="max"></span><span>✕</span></div>
  </header>

  <div class="toolbar">
    <svg style="left:20px" width="20" height="18" viewBox="0 0 20 18"><path d="M1 3h6l2 2h8v2H5L2 15H1z M5 8h14l-3 8H2z" fill="#fff"/></svg>
    <svg style="left:58px" width="18" height="18" viewBox="0 0 18 18"><path d="M2 2h11l3 3v11H2z" fill="none" stroke="#fff" stroke-width="2"/><rect x="5" y="3" width="6" height="4" fill="#fff"/><rect x="5" y="10" width="8" height="5" fill="#fff"/></svg>
    <svg style="left:95px" width="16" height="18" viewBox="0 0 16 18"><path d="M2 1h8l4 4v12H2z" fill="none" stroke="#fff" stroke-width="2"/><path d="M5 9h6M5 12h6" stroke="#fff" stroke-width="1.5"/></svg>
    <svg style="left:132px" width="18" height="18" viewBox="0 0 18 18"><path d="M1 3h16M1 9h16M1 15h16" stroke="#fff" stroke-width="2.5"/></svg>
    <svg style="left:168px" width="18" height="18" viewBox="0 0 18 18"><rect x="1" y="1" width="7" height="7" fill="#fff"/><rect x="10" y="1" width="7" height="7" fill="#fff"/><rect x="1" y="10" width="7" height="7" fill="#fff"/><rect x="10" y="10" width="7" height="7" fill="#fff"/></svg>
    <svg style="left:205px" width="20" height="18" viewBox="0 0 20 18"><path d="M1 2h7l2 2h9v12H1z" fill="#fff"/></svg>
    <svg style="left:243px" width="18" height="18" viewBox="0 0 18 18"><rect x="1" y="5" width="10" height="12" fill="none" stroke="#fff" stroke-width="2"/><rect x="6" y="1" width="10" height="12" fill="none" stroke="#fff" stroke-width="2"/></svg>
    <svg style="left:281px" width="16" height="18" viewBox="0 0 16 18"><path d="M4 17V2M1 5l3-4 3 4M12 1v15M9 13l3 4 3-4" stroke="#fff" stroke-width="2" fill="none"/></svg>
    <svg style="left:317px" width="22" height="18" viewBox="0 0 22 18"><rect x="1" y="2" width="20" height="14" rx="1" fill="none" stroke="#fff" stroke-width="2"/><rect x="1" y="6" width="20" height="3" fill="#fff"/></svg>
    <svg style="left:356px" width="16" height="18" viewBox="0 0 16 18"><path d="M1 1l14 8-14 8z" fill="#00c9ea"/></svg>
    <svg style="left:392px" width="18" height="18" viewBox="0 0 18 18"><path d="M9 1l5 5h-3v6H7V6H4z M1 13h3v2h10v-2h3v4H1z" fill="#fff"/></svg>
    <svg style="left:956px" width="22" height="18" viewBox="0 0 22 18"><path d="M2 6h4l10-5v16L6 12H2z M6 12l2 5" fill="none" stroke="#fff" stroke-width="2"/></svg>
    <svg style="left:994px" width="22" height="20" viewBox="0 0 22 20"><path d="M11 1l10 5H1z M2 17h18v2H2z M4 8h2v8H4zM9 8h2v8H9zM14 8h2v8h-2z" fill="#fff"/></svg>
    <svg style="left:1032px" width="18" height="18" viewBox="0 0 18 18"><circle cx="9" cy="9" r="7.5" fill="none" stroke="#fff" stroke-width="1.8"/><path d="M6.5 7a2.5 2.5 0 1 1 3.5 2.3c-.8.4-1 .8-1 1.7" fill="none" stroke="#fff" stroke-width="1.8"/><circle cx="9" cy="13.5" r="1" fill="#fff"/></svg>
  </div>

  <aside class="side" style="left:0;width:249px">
    <div class="tabhead" style="left:0;width:243px"></div>
    <div class="tab" style="left:4px;width:155px;padding-left:22px">Application Explore</div>
    <div class="tab-icons" style="left:185px">
      <svg width="10" height="10" viewBox="0 0 10 10"><path d="M1 3v6h6M4 6l5-5M6 1h3v3" stroke="#fff" fill="none" stroke-width="1.4"/></svg>
      <svg width="8" height="10" viewBox="0 0 8 10"><path d="M1 1h6M2 1v4L0 6h8L6 5V1M4 6v4" stroke="#fff" fill="#fff" stroke-width="1.2"/></svg>
      <svg width="9" height="10" viewBox="0 0 9 10"><path d="M1 2l7 7M8 2L1 9" stroke="#fff" stroke-width="2"/></svg>
    </div>
    <div class="bugbear"><span style="position:absolute;left:12px;font-size:10px">⌄</span>
      <span style="display:inline-flex;align-items:center;gap:6px"><svg width="13" height="12" viewBox="0 0 13 12"><rect x="5" y="0" width="3" height="3" fill="#00c9ea"/><rect x="0" y="8" width="3" height="3" fill="#00c9ea"/><rect x="5" y="8" width="3" height="3" fill="#00c9ea"/><rect x="10" y="8" width="3" height="3" fill="#00c9ea"/><path d="M6.5 3v5M1.5 8V6h10v2" stroke="#00c9ea" fill="none"/></svg>Bugbear</span>
    </div>

    <div class="tree-row" style="left:44px;top:112px"><span class="chev">⌄</span><svg class="ico" viewBox="0 0 12 12"><rect x="1" y="3" width="7" height="8" fill="none" stroke="#fff"/><rect x="4" y="1" width="7" height="8" fill="none" stroke="#fff"/></svg>Pages</div>
    <div class="tree-row" style="left:69px;top:141px"><span class="chev">›</span><svg class="ico" viewBox="0 0 12 12"><path d="M0 2h4l1 1h7v8H0z" fill="#fff"/></svg>Ticketer</div>
    <div class="tree-row" style="left:69px;top:169px"><span class="chev">›</span><svg class="ico" viewBox="0 0 12 12"><path d="M2 1h6l3 3v7H2z" fill="none" stroke="#fff"/><path d="M4 6h5M4 8h5" stroke="#fff"/></svg>AddBug</div>
    <div class="tree-row" style="left:69px;top:200px"><span class="chev">›</span><svg class="ico" viewBox="0 0 12 12"><path d="M2 1h6l3 3v7H2z" fill="none" stroke="#fff"/><path d="M4 6h5M4 8h5" stroke="#fff"/></svg>Home</div>
    <div class="tree-row" style="left:69px;top:228px"><span class="chev">›</span><svg class="ico" viewBox="0 0 12 12"><path d="M2 1h6l3 3v7H2z" fill="none" stroke="#fff"/><path d="M4 6h5M4 8h5" stroke="#fff"/></svg>ViewBug</div>
    <div class="tree-row" style="left:57px;top:258px"><span class="chev"></span><svg class="ico" viewBox="0 0 12 12"><path d="M0 2h12M0 6h12M0 10h12" stroke="#fff" stroke-width="1.6"/></svg>Types</div>
    <div class="tree-row" style="left:57px;top:289px"><span class="chev">›</span><svg class="ico" viewBox="0 0 12 12"><path d="M2 1h6l3 3v7H2z" fill="none" stroke="#fff"/><path d="M4 6h5M4 8h5" stroke="#fff"/></svg>Templates</div>
    <div class="tree-row" style="left:57px;top:317px"><span class="chev"></span><svg class="ico" viewBox="0 0 12 12"><path d="M11 1L5 7M1 11c0-3 1-4 3-4l1 1c0 2-1 3-4 3z" stroke="#fff" fill="#fff" stroke-width="1.5"/></svg>Styles</div>
    <div class="tree-row" style="left:57px;top:348px"><span class="chev"></span><svg class="ico" viewBox="0 0 12 12"><circle cx="6" cy="6" r="4" fill="none" stroke="#fff" stroke-width="3" stroke-dasharray="2 1.2"/><circle cx="6" cy="6" r="2.5" fill="#fff"/><circle cx="6" cy="6" r="1.2" fill="#4b4b4b"/></svg>Settings</div>
    <div class="tree-row" style="left:57px;top:378px"><span class="chev">›</span><svg class="ico" viewBox="0 0 12 12"><path d="M0 2h4l1 1h7v8H0z" fill="#fff"/></svg>EmbeddedFiles</div>
    <div class="tree-row" style="left:57px;top:409px"><span class="chev">›</span><svg class="ico" viewBox="0 0 12 12"><path d="M3 11V1M1 3l2-2 2 2M9 1v10M7 9l2 2 2-2" stroke="#fff" fill="none" stroke-width="1.4"/></svg>Connectors</div>
  </aside>

  <main class="work">
    <div class="tab" style="left:5px;top:2px;width:76px;padding-left:12px">View Bug</div>
    <div class="box shadowed boxlabel" style="left:6px;top:41px;width:113px;height:32px;padding-left:26px;font-weight:500"><span class="t">T</span>&nbsp;Lable 1</div>

    <div class="box" style="left:6px;top:83px;width:565px;height:416px">
      <div class="boxlabel" style="left:12px;top:8px"><span class="grid-ico"></span>Layout Panels</div>

      <div class="box shadowed" style="left:9px;top:29px;width:422px;height:375px">
        <div class="boxlabel" style="left:10px;top:8px"><span class="sq"></span>DetailsPanel</div>

        <div class="box" style="left:15px;top:38px;width:396px;height:126px;background:#fafafa">
          <div class="boxlabel" style="left:12px;top:8px"><span class="grid-ico"></span>LayoutTable2</div>
          <div class="cell" style="left:12px;top:39px;width:114px"><span class="t">T</span>Lable 3</div>
          <div class="cell" style="left:134px;top:39px;width:128px"><span class="t">T</span>ReportedByL...</div>
          <div class="cell" style="left:268px;top:39px;width:115px"><span class="t">T</span>Lable 2</div>
          <div class="cell" style="left:12px;top:78px;width:114px"><span class="t">T</span>ReportedOn...</div>
          <div class="cell" style="left:134px;top:78px;width:128px"><span class="t">T</span>ReportedByL...</div>
          <div class="cell" style="left:268px;top:78px;width:115px"><span class="t">T</span>StatusDropD...</div>
        </div>

        <div class="box" style="left:15px;top:179px;width:396px;height:86px;background:#fafafa">
          <div class="boxlabel" style="left:12px;top:8px"><span class="grid-ico"></span>LayoutTable4</div>
          <div class="cell" style="left:12px;top:39px;width:114px"><span class="t">T</span>TitleLabel</div>
          <div class="cell" style="left:134px;top:39px;width:128px"><span class="t">T</span>EditTitleImage</div>
          <div class="cell" style="left:268px;top:39px;width:115px"><span class="t">T</span>SaveTitleIma...</div>
        </div>

        <div class="box" style="left:15px;top:279px;width:396px;height:83px;background:#fafafa">
          <div class="boxlabel" style="left:12px;top:8px"><span class="grid-ico"></span>LayoutTable4</div>
          <div class="cell" style="left:12px;top:39px;width:114px"><span class="t">T</span>TitleLabel</div>
          <div class="cell" style="left:134px;top:39px;width:128px"><span class="t">T</span>EditDescripti...</div>
          <div class="cell" style="left:268px;top:39px;width:115px"><span class="t">T</span>SaveDescript...</div>
        </div>
      </div>

      <div class="box shadowed" style="left:437px;top:29px;width:119px;height:195px">
        <div class="boxlabel" style="left:12px;top:8px"><span class="sq"></span>Panel 1</div>
        <div class="cell" style="left:5px;top:38px;width:110px;height:30px"><span class="t">T</span>Label3</div>
        <div class="cell" style="left:5px;top:73px;width:110px;height:30px"><span class="grid-ico"></span>CommentData</div>
        <div class="cell" style="left:5px;top:108px;width:110px;height:30px"><span class="t">T</span>TextBox</div>
        <div class="cell" style="left:5px;top:144px;width:110px;height:30px"><svg width="11" height="10" viewBox="0 0 11 10"><path d="M1 1h9v6H5L2 9V7H1z" fill="none" stroke="#222"/></svg>Comment</div>
      </div>
    </div>
  </main>

  <section class="valid">
    <div class="bar"></div>
    <div class="tab">Validations</div>
    <div class="tab-icons" style="left:513px;top:13px">
      <svg width="10" height="10" viewBox="0 0 10 10"><path d="M1 3v6h6M4 6l5-5M6 1h3v3" stroke="#fff" fill="none" stroke-width="1.4"/></svg>
      <svg width="8" height="10" viewBox="0 0 8 10"><path d="M1 1h6M2 1v4L0 6h8L6 5V1M4 6v4" stroke="#fff" fill="#fff" stroke-width="1.2"/></svg>
      <svg width="9" height="10" viewBox="0 0 9 10"><path d="M1 2l7 7M8 2L1 9" stroke="#fff" stroke-width="2"/></svg>
    </div>
    <div class="vhead" style="left:19px">Description</div>
    <div class="vhead" style="left:242px">Path</div>
    <div class="vrow" style="top:80px"><span class="x">✕</span><span class="d">No page has been linked</span><span class="p">Pages &gt; StartPage &gt; Menu1 &gt; Menu Item 1&gt; Destination Page</span></div>
    <div class="vrow" style="top:99px"><span class="x">✕</span><span class="d">No page has been linked</span><span class="p">Pages &gt; StartPage &gt; Menu1 &gt; Menu Item 2 &gt; Menu Item 2.1...</span></div>
    <div class="vrow" style="top:119px"><span class="x">✕</span><span class="d">No page has been linked</span><span class="p">Pages &gt; StartPage &gt; Menu1 &gt; Menu Item 3 &gt; Menu Item 3.1...</span></div>
    <div class="vrow" style="top:138px"><span class="x">✕</span><span class="d">No page has been linked</span><span class="p">Pages &gt; StartPage &gt; Menu1 &gt; Menu Item 4 &gt; Destination Page</span></div>
  </section>

  <aside class="side rightp">
    <div class="tabhead" style="left:75px;width:170px"></div>
    <div class="tab" style="left:2px;width:70px;justify-content:center;padding:0">Toolbox</div>
    <div class="tab-icons" style="left:178px">
      <svg width="10" height="10" viewBox="0 0 10 10"><path d="M1 3v6h6M4 6l5-5M6 1h3v3" stroke="#fff" fill="none" stroke-width="1.4"/></svg>
      <svg width="8" height="10" viewBox="0 0 8 10"><path d="M1 1h6M2 1v4L0 6h8L6 5V1M4 6v4" stroke="#fff" fill="#fff" stroke-width="1.2"/></svg>
      <svg width="9" height="10" viewBox="0 0 9 10"><path d="M1 2l7 7M8 2L1 9" stroke="#fff" stroke-width="2"/></svg>
    </div>
    <div class="section" style="top:40px">View</div>
    <div class="tiles" style="top:82px">
      <div class="tile"><svg viewBox="0 0 12 12"><circle cx="6" cy="6" r="5" fill="none" stroke="#333"/><circle cx="6" cy="6" r="2.5" fill="#333"/></svg>Button</div>
      <div class="tile"><svg viewBox="0 0 12 12"><path d="M1 1v10h10M3 9V6M5 9V3M7 9V5M9 9V2" stroke="#333" fill="none" stroke-width="1.4"/></svg>Chart</div>
      <div class="tile"><svg viewBox="0 0 12 12"><rect x="1" y="1" width="10" height="10" fill="none" stroke="#333"/><path d="M3 6l2 2 4-5" stroke="#333" fill="none" stroke-width="1.4"/></svg>Chech Box</div>
      <div class="tile"><svg viewBox="0 0 12 12"><path d="M0 2h2M4 2h8M0 6h2M4 6h8M0 10h2M4 10h8" stroke="#333" stroke-width="1.6"/></svg>List</div>
      <div class="tile"><svg viewBox="0 0 12 12"><rect x="0" y="1" width="5" height="4" fill="#333"/><rect x="7" y="1" width="5" height="4" fill="#333"/><rect x="0" y="7" width="5" height="4" fill="#333"/><rect x="7" y="7" width="5" height="4" fill="#333"/></svg>Data Grid</div>
      <div class="tile"><svg viewBox="0 0 12 12"><rect x="1" y="2" width="10" height="9" fill="none" stroke="#333"/><path d="M1 4h10M3 6h2M6 6h2M3 8h2M6 8h2" stroke="#333"/></svg>Date Picker</div>
      <div class="tile"><svg viewBox="0 0 12 12"><path d="M6 1v9M2 6l4 4 4-4" stroke="#333" fill="none" stroke-width="1.8"/></svg>Drop Down</div>
      <div class="tile"><svg viewBox="0 0 12 12"><path d="M2 1h6l3 3v7H2z" fill="none" stroke="#333"/><path d="M3 10l3-3 2 2 1-1 1 2z" fill="#333"/></svg>Image</div>
      <div class="tile"><span style="font-family:'Roboto Slab',serif;font-weight:500;font-size:13px;line-height:12px">t</span>Label</div>
      <div class="tile active"><svg viewBox="0 0 12 12"><path d="M5 7l2-2M4 5L2 7a2 2 0 0 0 3 3l2-2M8 7l2-2a2 2 0 0 0-3-3L5 4" stroke="#fff" fill="none" stroke-width="1.5"/></svg>Link</div>
      <div class="tile"><svg viewBox="0 0 12 12"><path d="M1 2h10M1 6h10M1 10h10" stroke="#333" stroke-width="1.6"/></svg>Menu</div>
      <div class="tile"><svg viewBox="0 0 12 12"><rect x="1" y="1" width="10" height="10" fill="#333"/></svg>Panel</div>
      <div class="tile"><svg viewBox="0 0 12 12"><rect x="1" y="2" width="10" height="8" rx="1" fill="none" stroke="#333"/><path d="M3 5h6M3 7h6" stroke="#333"/></svg>Radio</div>
      <div class="tile"><svg viewBox="0 0 12 12"><path d="M10 6a4 4 0 1 1-1.5-3.1M9 1v3H6" stroke="#333" fill="none" stroke-width="1.6"/></svg>Repeater</div>
      <div class="tile"><svg viewBox="0 0 12 12"><rect x="1" y="2" width="9" height="9" fill="none" stroke="#333"/><path d="M5 7l6-6" stroke="#333" stroke-width="1.4"/></svg>Text Box</div>
      <div class="tile"><svg viewBox="0 0 12 12"><path d="M3 10a3 3 0 0 1 0-6 4 4 0 0 1 7 1 2.5 2.5 0 0 1 0 5z" fill="#333"/><path d="M6 9V5M4 7l2-2 2 2" stroke="#fff" fill="none"/></svg>Upload</div>
    </div>
    <div class="section" style="top:260px">Layout</div>
    <div class="tiles" style="top:302px">
      <div class="tile"><svg viewBox="0 0 12 12"><rect x="1" y="1" width="10" height="10" rx="2" fill="none" stroke="#333"/></svg>Container</div>
      <div class="tile"><svg viewBox="0 0 12 12"><circle cx="2" cy="6" r="1.2" fill="#333"/><circle cx="6" cy="6" r="1.2" fill="#333"/><circle cx="10" cy="6" r="1.2" fill="#333"/></svg>Flexbox</div>
      <div class="tile"><svg viewBox="0 0 12 12"><rect x="0" y="1" width="3" height="3" fill="#333"/><rect x="4.5" y="1" width="3" height="3" fill="#333"/><rect x="9" y="1" width="3" height="3" fill="#333"/><rect x="0" y="5" width="3" height="3" fill="#333"/><rect x="4.5" y="5" width="3" height="3" fill="#333"/><rect x="9" y="5" width="3" height="3" fill="#333"/><rect x="0" y="9" width="3" height="3" fill="#333"/><rect x="4.5" y="9" width="3" height="3" fill="#333"/><rect x="9" y="9" width="3" height="3" fill="#333"/></svg>Grid</div>
      <div class="tile"><svg viewBox="0 0 12 12"><rect x="1" y="1" width="10" height="10" fill="none" stroke="#333"/><path d="M1 4h10M1 7.5h10M4.5 1v10M8 1v10" stroke="#333"/></svg>Table</div>
    </div>
    <div class="tabhead" style="left:148px;top:349px;width:97px;height:31px"></div>
    <div class="tab" style="left:2px;top:349px;width:143px;justify-content:center;padding:0">Properties (DataGrid)</div>
    <div class="tab-icons" style="left:178px;top:359px">
      <svg width="10" height="10" viewBox="0 0 10 10"><path d="M1 3v6h6M4 6l5-5M6 1h3v3" stroke="#fff" fill="none" stroke-width="1.4"/></svg>
      <svg width="8" height="10" viewBox="0 0 8 10"><path d="M1 1h6M2 1v4L0 6h8L6 5V1M4 6v4" stroke="#fff" fill="#fff" stroke-width="1.2"/></svg>
      <svg width="9" height="10" viewBox="0 0 9 10"><path d="M1 2l7 7M8 2L1 9" stroke="#fff" stroke-width="2"/></svg>
    </div>
    <div class="prop" style="top:387px">Name<span class="v" style="width:149px">HistoryDataGrid</span></div>
    <div class="prop" style="top:418px">Columns<span class="v" style="width:149px">(Collection)<svg style="position:absolute;right:2px;top:2px" width="18" height="18" viewBox="0 0 18 18"><rect width="18" height="18" fill="#555"/><path d="M4 6v8h8M8 10l6-6" stroke="#fff" fill="none" stroke-width="1.3"/></svg></span></div>
    <div class="prop" style="top:449px">Allow Export<span class="chk"></span></div>
    <div class="prop" style="top:480px">Display Bar<span class="chk"></span></div>
    <div class="prop" style="top:511px">Selectable Data<span class="chk"></span></div>
    <div class="prop" style="top:542px">Selectable Data<span class="v" style="width:149px">True<svg style="position:absolute;right:2px;top:2px" width="18" height="18" viewBox="0 0 18 18"><rect x=".5" y=".5" width="17" height="17" fill="#fff" stroke="#555"/><path d="M6 8l3 3 3-3" stroke="#333" fill="none"/></svg></span></div>
    <div class="help">Property Help<svg style="position:absolute;right:8px;top:14px" width="8" height="5" viewBox="0 0 8 5"><path d="M1 1l3 3 3-3" stroke="#333" fill="none"/></svg></div>
  </aside>

  <footer class="footer">Copyrights 2021 VORLIX. All Rights Reserved<span class="ver">C45</span></footer>
</section>

<section class="frame" style="top:981px;height:1039px">
  <header class="titlebar">
    <div class="brand"><i></i>Vorlix</div>
    <div class="win-title">Columns</div>
    <div class="win-btns"><span class="max"></span><span>✕</span></div>
  </header>
  <h1 class="dialog-title">ADD COLOUMN</h1>

  <div class="card" style="top:168px;height:214px"></div>
  <div class="field" style="left:142px;top:196px;width:389px">First Name</div>
  <div class="field" style="left:541px;top:196px;width:389px">Last Name</div>
  <div class="field" style="left:142px;top:253px;width:389px">Height</div>
  <div class="field" style="left:541px;top:253px;width:389px">Age</div>
  <div class="btn-primary" style="left:341px;top:311px;width:388px;height:42px">ADD COLOUMN</div>

  <div class="card" style="top:435px;height:478px"></div>
  <div class="flabel" style="left:142px;top:468px">Column Type</div>
  <div class="field" style="left:142px;top:496px;width:389px">Data-Bound<span class="drop"><svg width="12" height="8" viewBox="0 0 12 8"><path d="M1 1l5 5 5-5" stroke="#222" fill="none" stroke-width="1.6"/></svg></span></div>
  <div class="flabel" style="left:541px;top:468px">Text</div>
  <div class="field" style="left:541px;top:496px;width:389px">(Data-Bound)</div>
  <div class="flabel" style="left:142px;top:560px">Click</div>
  <div class="field" style="left:142px;top:588px;width:389px">Create Event Handler</div>
  <div class="flabel" style="left:541px;top:560px">Header Text</div>
  <div class="field" style="left:541px;top:588px;width:389px">First Name<span class="drop"><svg width="12" height="8" viewBox="0 0 12 8"><path d="M1 1l5 5 5-5" stroke="#222" fill="none" stroke-width="1.6"/></svg></span></div>
  <div class="flabel" style="left:142px;top:652px">Alignment</div>
  <div class="field" style="left:142px;top:680px;width:389px">Left<span class="drop"><svg width="12" height="8" viewBox="0 0 12 8"><path d="M1 1l5 5 5-5" stroke="#222" fill="none" stroke-width="1.6"/></svg></span></div>
  <div class="flabel" style="left:541px;top:652px">Cell Display</div>
  <div class="field" style="left:541px;top:680px;width:389px">Default<span class="drop"><svg width="12" height="8" viewBox="0 0 12 8"><path d="M1 1l5 5 5-5" stroke="#222" fill="none" stroke-width="1.6"/></svg></span></div>
  <div class="expander" style="left:142px;top:744px"><svg width="10" height="7" viewBox="0 0 10 7"><path d="M1 1l4 4 4-4" stroke="#222" fill="none" stroke-width="1.5"/></svg>Column Type</div>
  <div class="help-text" style="left:142px;top:775px">Choose whether the cell displays a value from a connector or the specified text</div>
  <div class="btn-primary" style="left:413px;top:833px;width:117px;height:43px">SAVE</div>
  <div class="btn-outline" style="left:540px;top:833px;width:117px;height:43px">CANCEL</div>

  <footer class="footer">Copyrights 2021 VORLIX. All Rights Reserved<span class="ver">C45</span></footer>
</section>

<section class="frame" style="top:2082px;height:1039px">
  <header class="titlebar">
    <div class="brand"><i></i>Vorlix</div>
    <div class="win-title">Columns</div>
    <div class="win-btns"><span class="max"></span><span>✕</span></div>
  </header>
  <h1 class="dialog-title">ADD COLOUMN</h1>

  <div class="card" style="top:168px;height:214px"></div>
  <div class="field" style="left:142px;top:196px;width:389px">First Name</div>
  <div class="field" style="left:541px;top:196px;width:389px">Last Name</div>
  <div class="field" style="left:142px;top:253px;width:389px">Height</div>
  <div class="field" style="left:541px;top:253px;width:389px">Age</div>
  <div class="btn-primary" style="left:341px;top:311px;width:388px;height:42px">ADD COLOUMN</div>

  <div class="card" style="top:435px;height:478px"></div>
  <div class="flabel" style="left:142px;top:468px">Column Type</div>
  <div class="field" style="left:142px;top:496px;width:389px">Data-Bound<span class="drop"><svg width="12" height="8" viewBox="0 0 12 8"><path d="M1 1l5 5 5-5" stroke="#222" fill="none" stroke-width="1.6"/></svg></span></div>
  <div class="flabel" style="left:541px;top:468px">Text</div>
  <div class="field" style="left:541px;top:496px;width:389px">(Data-Bound)</div>
  <div class="flabel" style="left:142px;top:560px">Click</div>
  <div class="field" style="left:142px;top:588px;width:389px">Create Event Handler</div>
  <div class="flabel" style="left:541px;top:560px">Header Text</div>
  <div class="field" style="left:541px;top:588px;width:389px">First Name<span class="x2" style="position:absolute;right:54px;color:#111">X2</span><span class="drop"><svg width="12" height="8" viewBox="0 0 12 8"><path d="M1 7l5-5 5 5" stroke="#222" fill="none" stroke-width="1.6"/></svg></span></div>
  <div class="flabel" style="left:142px;top:652px">Alignment</div>
  <div class="field" style="left:142px;top:680px;width:389px">Left<span class="drop"><svg width="12" height="8" viewBox="0 0 12 8"><path d="M1 1l5 5 5-5" stroke="#222" fill="none" stroke-width="1.6"/></svg></span></div>
  <div class="expander" style="left:142px;top:744px"><svg width="10" height="7" viewBox="0 0 10 7"><path d="M1 1l4 4 4-4" stroke="#222" fill="none" stroke-width="1.5"/></svg>Column Type</div>
  <div class="help-text" style="left:142px;top:775px">Choose whether the cell displays a value from a connector or the specified text</div>

  <div class="picker" style="top:632px">
    <div style="left:12px;top:8px"><span class="x2">X2</span>Expression</div>
    <div style="left:28px;top:34px"><svg width="9" height="6" viewBox="0 0 9 6"><path d="M1 1l3.5 3.5L8 1" stroke="#222" fill="none" stroke-width="1.4"/></svg>Season</div>
    <div style="left:57px;top:59px"><svg width="9" height="6" viewBox="0 0 9 6"><path d="M1 1l3.5 3.5L8 1" stroke="#222" fill="none" stroke-width="1.4"/></svg>LoggedInUser</div>
    <div class="leaf" style="left:84px;top:86px">ID</div>
    <div class="leaf" style="left:84px;top:105px">Name</div>
    <div class="leaf" style="left:84px;top:123px">Email</div>
    <div class="leaf" style="left:84px;top:142px">Roles</div>
  </div>

  <div class="btn-primary" style="left:413px;top:833px;width:117px;height:43px">SAVE</div>
  <div class="btn-outline" style="left:540px;top:833px;width:117px;height:43px">CANCEL</div>

  <footer class="footer">Copyrights 2021 VORLIX. All Rights Reserved<span class="ver">C45</span></footer>
</section>

</body>
</html>
```